Tidewell Homes Website Redesign

We need a website redesign for an existing website www.tidewellhomes.com.au. A home page and a property page needs to be designed...have attached layout for property page which sits under House and Land.

Have also attached logo.

Site will be built on Pane Core Hub 5x content management system so design needs to be PCH compatible and using system fonts as well eg Arial, Verdana or Tahoma.

Target Market(s)

Builders and owner builders

Industry/Entity Type

Construction

Number of Pages Required

2 pages

Requirements
Must have
• Site Map

• o Home
• o Inclusions
• o Designs
• o House and Land
• ? Gallery
• o Selection Centre
• o Redevelopment
• o Contact Us

• Design Brief

• o Likes www.corvanstone.com.au as a corporate homepage layout...with buttons across the bottom etc
• o Likes http://www.belvarra.com.au/
• o Likes http://www.quorrin.com.au/, but this site is built entirely in flash so some functionality won’t be possible.
• • Logo and phone number across top 02 6387 2915
• • Rolling banner along bottom of page with gallery photos
• • Horizontal navigational bar
• • Content below the main menu
• • Large contact us button.
• - Need to ensure BTU and Guild Framer logo is on every page (perhaps in footer???)
• - Need
• ACN 071 352 908 NSW License No. 438251K ACT License No. 3142
• also in footer of every page

• Colours are, maroon, gold and predominately white. I don"t have any problems with some elements of light grey.

```html
<!DOCTYPE html>
<html lang="en">
<head>
<meta charset="utf-8">
<title>Tidewell Homes – Home and Property Page</title>
<link rel="stylesheet" href="https://fonts.googleapis.com/css2?family=Arimo:wght@400;700&display=swap">
<style>
:root{
  --maroon:#6a0e3b;
  --maroon-dark:#570a30;
  --gold:#b8ab68;
  --gold-light:#d8cf9c;
  --sky:#d3f0fb;
  --panel-top:#e4e1c0;
  --text:#3a3a3a;
  --white:#ffffff;
  --badge-navy:#1d2a6b;
  --badge-green:#1f6b45;
}
*{box-sizing:border-box;margin:0;padding:0}
html,body{width:1200px;height:2776px;overflow:hidden;background:var(--white);font-family:Arimo,Arial,sans-serif;color:var(--text)}
.page{position:absolute;left:0;width:1200px;background:linear-gradient(var(--sky) 0,#eef9fd 420px,#fff 700px,#fff calc(100% - 260px),var(--sky) 100%);border-top:4px solid var(--maroon);border-image:linear-gradient(90deg,var(--maroon),var(--gold)) 1}
.page--home{top:0;height:1183px}
.page--property{top:1289px;height:1487px}
.page-label{position:absolute;top:1228px;width:1200px;text-align:center;font-size:26px;color:#111}
.rule-v{position:absolute;left:144px;top:100px;width:2px;background:linear-gradient(transparent,var(--gold-light) 10%,var(--gold-light) 90%,transparent)}
.rule-h{position:absolute;left:99px;width:1000px;height:2px;background:linear-gradient(90deg,transparent,var(--maroon) 8%,var(--gold-light) 60%,transparent)}
.brand{position:absolute;left:162px;top:58px;display:flex;align-items:center;gap:10px;font-size:32px;font-weight:700;color:var(--maroon)}
.brand-dot{width:14px;height:14px;border-radius:50%;background:var(--gold)}
.callout{position:absolute;right:152px;top:96px;font-size:20px;color:var(--gold)}
.callout b{color:var(--maroon)}
.nav{position:absolute;left:146px;top:153px;width:902px;height:46px;background:var(--maroon);display:flex;align-items:center;justify-content:space-between;padding:0 24px;list-style:none}
.nav li{font-size:12.5px;font-weight:700;color:var(--white)}
.nav li.is-active{color:var(--gold)}
.banner{position:absolute;left:153px;top:213px;width:894px;height:310px;border:2px solid var(--maroon);background:linear-gradient(160deg,#8c8a5e,#c9a25a 45%,#8f7a5a 70%,#6d6a58)}
.banner-caption{position:absolute;left:0;bottom:0;width:100%;height:70px;background:rgba(40,40,40,.75);display:flex;align-items:center;justify-content:space-between;padding:0 28px 0 32px}
.banner-caption q{font-size:25px;font-style:italic;color:var(--white)}
.pager{display:flex;gap:5px}
.pager span{width:18px;height:18px;background:var(--gold);color:#fff;font-size:11px;font-weight:700;text-align:center;line-height:18px}
.pager span.is-current{background:#d8c35a;color:#333}
.arrow{position:absolute;top:348px;width:40px;height:40px;border-radius:50%;background:#fff;border:2px solid var(--gold-light)}
.arrow svg{display:block;margin:10px}
.panel{position:absolute;left:153px;width:894px;background:linear-gradient(var(--panel-top),#fff 240px)}
.panel--home{top:523px;height:439px}
.panel--property{top:213px;height:1052px}
.heading{font-size:21px;font-weight:400;color:#333}
.heading b{color:var(--maroon)}
.welcome{position:absolute;left:19px;top:17px;width:605px}
.welcome p{font-size:12px;line-height:17.8px;margin-top:17.5px}
.welcome .heading{margin-bottom:20px}
.recent{position:absolute;left:644px;top:17px;width:230px}
.recent-photo{margin-top:18px;width:230px;height:161px;border:1px solid #ccc;background:linear-gradient(#5f6fb8,#aab6d8 45%,#8c9b6b 70%,#5d7a3d)}
.recent h3{font-size:12px;margin:14px 0 6px 12px;color:#222}
.recent p{font-size:12px;line-height:17.8px;margin-left:12px;width:200px}
.more{display:block;text-align:right;margin-top:14px;font-size:12px;font-weight:700;color:var(--maroon)}
.more::before{content:"";display:inline-block;border:3px solid transparent;border-left:4px solid var(--maroon);margin-right:3px}
.footer{position:absolute;left:0;width:1140px;text-align:center}
.footer-links{font-size:12px;font-weight:700;color:var(--maroon);word-spacing:1px}
.footer-links span{color:#555;font-weight:400;margin:0 5px}
.footer-copy{font-size:10.5px;margin-top:6px;color:#444}
.footer-acn{font-size:12px;margin-top:15px;color:#333}
.badges{display:flex;justify-content:center;gap:16px;margin-top:18px}
.badge-a{width:116px;height:86px;border-radius:8px;background:var(--badge-navy)}
.badge-b{width:72px;height:86px;border-radius:14px 14px 36px 36px;background:var(--badge-green)}
.title{position:absolute;left:19px;top:16px;font-size:21px;font-weight:700;color:var(--maroon);word-spacing:14px}
.photo-main{position:absolute;left:19px;top:58px;width:606px;height:452px;border:6px solid #fff;outline:1px solid #ccc;background:linear-gradient(170deg,#8d9064,#c29458 45%,#6f6a5c 70%,#9e9486)}
.thumb{position:absolute;left:644px;width:230px;height:147px;border:6px solid #fff;outline:1px solid #ccc}
.thumb--1{top:58px;background:linear-gradient(90deg,#a89a86,#d8d0c2 50%,#7e8f9e)}
.thumb--2{top:211px;background:linear-gradient(#7d6a5a,#b8a78f 50%,#c9763f)}
.thumb--3{top:364px;background:linear-gradient(135deg,#d9b86a,#efdca9 60%,#c8a35c)}
.flyer{position:absolute;left:19px;top:528px;width:603px;height:409px;background:linear-gradient(#fbfbfd,#eef0f4)}
.specs{position:absolute;left:644px;top:558px;width:229px;height:143px;border:2px solid var(--maroon);background:#fff}
.specs h4{height:31px;background:var(--maroon);color:#fff;font-size:12.5px;padding:8px 11px;position:relative}
.specs h4::after{content:"";position:absolute;left:20px;bottom:-8px;border:8px solid transparent;border-bottom:0;border-top-color:var(--maroon)}
.specs dl{display:grid;grid-template-columns:116px 1fr;row-gap:2px;padding:20px 0 0 24px;font-size:12px}
.specs dt{font-weight:700;color:#333}
.cta{position:absolute;left:644px;top:723px;width:183px;height:43px;border-radius:22px;border:3px solid var(--maroon);background:linear-gradient(#e6dfa8,#b9ad62);display:flex;align-items:center;justify-content:center;gap:8px;font-size:16px;font-weight:700;color:var(--maroon)}
.blurb{position:absolute;left:19px;top:952px;width:605px;font-size:12px;line-height:17.8px}
</style>
</head>
<body>

<section class="page page--home">
  <div class="rule-v" style="height:910px"></div>
  <div class="brand"><span class="brand-dot"></span>Tidewell Homes</div>
  <p class="callout">Call us today! <b>02 6387 2915</b></p>
  <ul class="nav">
    <li class="is-active">HOME</li><li>INCLUSIONS</li><li>DESIGNS</li><li>HOUSE AND LAND</li><li>GALLERY</li><li>SELECTION CENTRE</li><li>REDEVELOPMENT</li><li>CONTACT US</li>
  </ul>
  <div class="rule-h" style="top:199px"></div>

  <div class="arrow" style="left:101px"><svg width="16" height="16" viewBox="0 0 16 16"><path d="M11 2 5 8l6 6" fill="none" stroke="#6a0e3b" stroke-width="3"/></svg></div>
  <div class="arrow" style="left:1059px"><svg width="16" height="16" viewBox="0 0 16 16"><path d="M5 2l6 6-6 6" fill="none" stroke="#6a0e3b" stroke-width="3"/></svg></div>
  <div class="banner" role="img" aria-label="Rotating gallery photo of a finished home with timber deck at dusk">
    <div class="banner-caption">
      <q>We will build your home on budget and on time</q>
      <div class="pager"><span class="is-current">1</span><span>2</span><span>3</span><span>4</span><span>5</span></div>
    </div>
  </div>

  <div class="panel panel--home">
    <div class="welcome">
      <h2 class="heading">Welcome to <b>Tidewell Homes</b></h2>
      <p>Tidewell Homes was established in February 2001 by Owen Hartley and Callum Reeve. Between the two directors the company has over 40 years building experience in the ACT Region and both directors are individually licensed builders.</p>
      <p>We offer a range of flexible and varied home designs, these designs can be built on your land or ours. We will also quote individual designs should one of our plans be unsuitable to your needs or should you desire a more customized home.</p>
      <p>Tidewell Homes is a member of the Building Trades Union and Guild Framers Association. In addition both directors of the company are also accredited “Leafwise Professionals”.</p>
      <p>Tidewell Homes uses only quality suppliers and our team of contractors are reliable, qualified and assist us to achieve a quality finish.</p>
      <p>Both directors are hands on and personally oversee the construction process as well as being available to owners to attend to queries or concerns. Our aim is to build quality project homes whilst providing a boutique style service.</p>
      <p>Our efficient management of the construction process and our reliable team of contractors will ensure your new home is finished on time. This is why the Tidewell Homes guarantee is:</p>
    </div>
    <aside class="recent">
      <h2 class="heading">Recent <b>Designs</b></h2>
      <div class="recent-photo" role="img" aria-label="Facade render of a single storey home with floor plan inset"></div>
      <h3>Marlow 202</h3>
      <p>The best feature of this plan is that the kitchen divides the formal and informal living areas, whilst looking out over a covered outdoor area</p>
      <a class="more">LEAR MORE</a>
    </aside>
  </div>

  <div class="rule-h" style="top:962px"></div>
  <footer class="footer" style="top:984px">
    <p class="footer-links">Home<span>|</span>Inclusions<span>|</span>Designs<span>|</span>House and Land<span>|</span>Gallery<span>|</span>Selection Centre<span>|</span>Redevelopment<span>|</span>Contact US</p>
    <p class="footer-copy">© Tidewell Homes 2004 Owned and operated by MERT ( Canberra ) Pty Limited</p>
    <p class="footer-acn">ACN 071 352 908 NSW <b>License No. 438251K ACT License No. 3142</b></p>
    <div class="badges"><div class="badge-a" role="img" aria-label="Guild Framer membership badge"></div><div class="badge-b" role="img" aria-label="BTU membership badge"></div></div>
  </footer>
</section>

<p class="page-label">INNER PAGE</p>

<section class="page page--property">
  <div class="rule-v" style="height:1230px"></div>
  <div class="brand"><span class="brand-dot"></span>Tidewell Homes</div>
  <p class="callout">Call us today! <b>02 6387 2915</b></p>
  <ul class="nav">
    <li class="is-active">HOME</li><li>INCLUSIONS</li><li>DESIGNS</li><li>HOUSE AND LAND</li><li>GALLERY</li><li>SELECTION CENTRE</li><li>REDEVELOPMENT</li><li>CONTACT US</li>
  </ul>
  <div class="rule-h" style="top:199px"></div>

  <div class="panel panel--property">
    <h1 class="title">Suburb $400,000</h1>
    <div class="photo-main" role="img" aria-label="Main property photo of the home and timber deck at dusk"></div>
    <div class="thumb thumb--1" role="img" aria-label="Exterior detail photos of rendered walls and windows"></div>
    <div class="thumb thumb--2" role="img" aria-label="Kitchen interior photo with island bench"></div>
    <div class="thumb thumb--3" role="img" aria-label="Bathroom photo with freestanding bath"></div>
    <div class="flyer" role="img" aria-label="Home design flyer with price, feature list, elevation sketch and floor plan"></div>
    <section class="specs">
      <h4>SPECIFICATIONS</h4>
      <dl>
        <dt>Living Area:</dt><dd>202.3 sqm</dd>
        <dt>Garage:</dt><dd>40.2sqm</dd>
        <dt>Portico:</dt><dd>4.2sqm</dd>
        <dt>Outdoor Dining:</dt><dd>10.5sqm</dd>
      </dl>
    </section>
    <a class="cta">CONTACT US <svg width="7" height="10" viewBox="0 0 7 10"><path d="M0 0l7 5-7 5z" fill="#6a0e3b"/></svg></a>
    <p class="blurb">The best feature of this plan is that the kitchen divides the formal and informal living areas, whilst looking out over a covered outdoor area. Generous sized rooms and an open plan make this a must consider. Excellent when North is to the side but will also suit North to the front or rear. As our narrowest plan the Marlow series lend themselves to most narrow blocks.</p>
  </div>

  <div class="rule-h" style="top:1265px"></div>
  <footer class="footer" style="top:1286px">
    <p class="footer-links">Home<span>|</span>Inclusions<span>|</span>Designs<span>|</span>House and Land<span>|</span>Gallery<span>|</span>Selection Centre<span>|</span>Redevelopment<span>|</span>Contact US</p>
    <p class="footer-copy">© Tidewell Homes 2004 Owned and operated by MERT ( Canberra ) Pty Limited</p>
    <p class="footer-acn">ACN 071 352 908 NSW <b>License No. 438251K ACT License No. 3142</b></p>
    <div class="badges"><div class="badge-a" role="img" aria-label="Guild Framer membership badge"></div><div class="badge-b" role="img" aria-label="BTU membership badge"></div></div>
  </footer>
</section>

</body>
</html>
```